Blue Harbor Trophies & Awards Unique Business Card Design

Recently selected a new logo design and waiting to recieve print files. I've attached image for your review. We are a trophies and awards company that provides engraving on trophies, plaques, name plates, name tags, desk sets, medals, acrylics, and signage.

We are located in Monroe, Louisiana and provide this service with computerized & laser engraving equipment.

Target Market(s)

Corporate, Sport, Church, and Special Events

Industry/Entity Type

Business

Contact Information for Business Card

I'd like to see the following list on the card: Trophies, Plaques, Name Plates, Name Tags, Desk Sets, Medals, Certificates... this is accomplished with Computerized & Laser Engraving

Colors
0555a3
ec1f27
ffffff

Requirements
Must have
• I like either single or double sided. If a design can be created with a frosted card stock I'd consider single. Must be Red, White, and Blue. Dale Penrow - Owner, 415 W 9th Ave, Monroe, La 70384 office 318-555-2190 fax 318-555-2186 email: blueharbor@blueharbortrophyco.example, and website: www.blueharbortrophyco.example

```html
<!DOCTYPE html>
<html lang="en">
<head>
<meta charset="utf-8">
<title>Blue Harbor Trophies &amp; Awards – Business Card</title>
<link rel="stylesheet" href="https://fonts.googleapis.com/css2?family=Questrial&family=Great+Vibes&display=swap">
<style>
  :root {
    --page-bg: #e9e6e1;
    --card-white: #f6f7f8;
    --card-frost: #e3e8ee;
    --brand-blue: #0555a3;
    --deep-blue: #1d3f7a;
    --brand-red: #ec1f27;
    --red-dark: #a8121c;
    --red-mid: #c81a24;
    --ink-light: #f3e9ea;
    --star-grey: #e6d5d6;
  }
  html, body {
    margin: 0;
    padding: 0;
    width: 1200px;
    height: 970px;
    overflow: hidden;
    background: var(--page-bg);
  }
  .canvas {
    position: relative;
    width: 1200px;
    height: 970px;
  }
  .card {
    position: absolute;
    left: 120px;
    top: 218px;
    width: 960px;
    height: 534px;
    background: linear-gradient(180deg, var(--card-white) 0%, var(--card-frost) 100%);
    box-shadow: 0 10px 30px rgba(0,0,0,0.18);
    overflow: hidden;
    font-family: "Questrial", "Century Gothic", sans-serif;
  }
  .brand {
    position: absolute;
    left: 0;
    right: 0;
    top: 80px;
    text-align: center;
    font-size: 50px;
    color: var(--brand-blue);
    letter-spacing: 0.5px;
  }
  .rule {
    position: absolute;
    left: 0;
    right: 0;
    top: 214px;
    height: 3px;
    background: var(--brand-red);
  }
  .band {
    position: absolute;
    left: 0;
    right: 0;
    top: 222px;
    bottom: 0;
    background: linear-gradient(100deg, #c4303a 0%, var(--red-mid) 35%, var(--red-dark) 62%, var(--brand-red) 85%, var(--red-mid) 100%);
  }
  .person {
    position: absolute;
    left: 56px;
    top: 240px;
  }
  .person-name {
    font-family: "Great Vibes", cursive;
    font-size: 50px;
    color: var(--deep-blue);
    line-height: 1;
    margin: 0;
  }
  .person-role {
    margin: 12px 0 0;
    font-size: 20px;
    color: var(--ink-light);
  }
  .contact {
    position: absolute;
    left: 56px;
    top: 366px;
    width: 540px;
    margin: 0;
    padding: 0;
    list-style: none;
    color: var(--ink-light);
    font-size: 21px;
  }
  .contact li {
    display: flex;
    align-items: flex-start;
    gap: 22px;
    line-height: 24px;
    margin-bottom: 8px;
    white-space: nowrap;
  }
  .contact svg {
    width: 22px;
    height: 22px;
    flex: none;
    margin-top: 1px;
  }
  .services {
    position: absolute;
    left: 623px;
    top: 250px;
  }
  .services-title {
    font-family: "Great Vibes", cursive;
    font-size: 36px;
    color: var(--deep-blue);
    margin: 0 0 16px;
  }
  .services-list {
    margin: 0;
    padding: 0;
    list-style: none;
    color: var(--ink-light);
    font-size: 24px;
    line-height: 28px;
  }
  .services-list li::before {
    content: "★";
    color: var(--star-grey);
    font-size: 15px;
    display: inline-block;
    width: 32px;
  }
</style>
</head>
<body>
<div class="canvas">
  <div class="card">
    <div class="brand">Blue Harbor Trophies &amp; Awards</div>
    <div class="rule"></div>
    <div class="band"></div>

    <div class="person">
      <p class="person-name">Dale Penrow</p>
      <p class="person-role">Owner</p>
    </div>

    <ul class="contact">
      <li>
        <svg viewBox="0 0 24 24" aria-hidden="true"><path fill="#f3e9ea" d="M6.6 10.8a15 15 0 0 0 6.6 6.6l2.2-2.2c.3-.3.7-.4 1-.2 1.1.4 2.3.6 3.6.6.6 0 1 .4 1 1V20c0 .6-.4 1-1 1A17 17 0 0 1 3 4c0-.6.4-1 1-1h3.5c.6 0 1 .4 1 1 0 1.3.2 2.5.6 3.6.1.3 0 .7-.2 1z"/></svg>
        <span>318-555-2190</span>
      </li>
      <li>
        <svg viewBox="0 0 24 24" aria-hidden="true"><rect x="2" y="5" width="20" height="14" fill="#f3e9ea"/><path d="M2 5l10 8 10-8" fill="none" stroke="#b0141d" stroke-width="1.6"/></svg>
        <span>blueharbor@blueharbortrophyco.example</span>
      </li>
      <li>
        <svg viewBox="0 0 24 24" aria-hidden="true"><circle cx="12" cy="12" r="10" fill="#f3e9ea"/><path d="M7 7c2 1 3 3 2 5s1 3 2 5M14 4c-1 2 1 3 3 3s2 3 1 5" fill="none" stroke="#b0141d" stroke-width="1.6"/></svg>
        <span>www.blueharbortrophyco.example</span>
      </li>
      <li>
        <svg viewBox="0 0 24 24" aria-hidden="true"><path fill="#f3e9ea" d="M12 1a8 8 0 0 0-8 8c0 6 8 14 8 14s8-8 8-14a8 8 0 0 0-8-8z"/><circle cx="12" cy="9" r="3" fill="#b0141d"/></svg>
        <span>415 W 9th Ave<br>Monroe, LA&nbsp; 70384</span>
      </li>
    </ul>

    <div class="services">
      <p class="services-title">Services</p>
      <ul class="services-list">
        <li>engraving on trophies</li>
        <li>plaques</li>
        <li>name plates</li>
        <li>name tags</li>
        <li>desk sets</li>
        <li>medals</li>
        <li>acrylics, and signage</li>
      </ul>
    </div>
  </div>
</div>
</body>
</html>
```